Marlow Hire Business Card for recruitment company

We are looking for a Business Card Design that incorporates our personal details and our busines name and logo. We are a specialized search consultancy that recruit Property and Construction professionals.
We would like a business card that stands out and is appealing to the Construction and Property industry as well.

Target Market(s)

people in the construction and property industry

Contact Information for Business Card

Business Name and logo

Font styles to use
Serif

Colors
0094D4
00A9DD
6FCCEA
C7EBF8
E9F6FB

Requirements
Must have
• Business name and logo as well as contact details
Should not have
• No photos of us please

```html
<!DOCTYPE html>
<html lang="en">
<head>
<meta charset="utf-8">
<title>Marlow Hire — Business Card</title>
<link href="https://fonts.googleapis.com/css2?family=Montserrat:wght@400;500;600&display=swap" rel="stylesheet">
<style>
  :root {
    --stage: #bcbdbf;
    --front: #c8eaf8;
    --back: #eaf6fc;
    --speck: #6fccea;
    --ink-brand: #0f3a4e;
    --ink-name: #111111;
    --ink-body: #333333;
    --rule: #1a1a1a;
  }
  * { margin: 0; padding: 0; box-sizing: border-box; }
  html, body { width: 1200px; height: 1000px; overflow: hidden; }
  body {
    background: var(--stage);
    font-family: "Montserrat", Arial, sans-serif;
    position: relative;
  }
  .card {
    position: absolute;
    top: 340px;
    width: 496px;
    height: 320px;
    overflow: hidden;
  }
  .card--front { left: 61px; background: var(--front); }
  .card--back { left: 644px; background: var(--back); }
  .texture {
    position: absolute; inset: 0;
  }
  .card--front .texture {
    background: radial-gradient(ellipse at 72% 40%, rgba(111,204,234,0.45), rgba(111,204,234,0) 60%);
  }
  .card--back .texture {
    background: radial-gradient(ellipse at 30% 25%, rgba(199,235,248,0.9), rgba(199,235,248,0) 60%);
  }
  .brand {
    position: absolute;
    color: var(--ink-brand);
    font-weight: 400;
    text-transform: uppercase;
    white-space: nowrap;
  }
  .card--front .brand {
    left: 0; right: 0; top: 138px;
    text-align: center;
    font-size: 41px;
    letter-spacing: 2px;
  }
  .card--back .brand {
    right: 20px; top: 30px;
    font-size: 17px;
    letter-spacing: 0.5px;
  }
  .person { position: absolute; left: 21px; top: 122px; }
  .person__name { font-size: 26px; font-weight: 600; color: var(--ink-name); letter-spacing: 0.3px; }
  .person__role { font-size: 19px; color: var(--ink-body); margin-top: 4px; }
  .divider {
    position: absolute; left: 21px; top: 207px;
    width: 225px; height: 2px; background: var(--rule);
  }
  .contacts { position: absolute; left: 21px; top: 219px; list-style: none; }
  .contacts li {
    display: flex; align-items: center; gap: 8px;
    font-size: 15.5px; color: var(--ink-body); height: 27px;
  }
  .contacts svg { width: 14px; height: 14px; fill: var(--ink-brand); }
  .website {
    position: absolute; right: 20px; top: 270px;
    font-size: 15.5px; color: var(--ink-body);
  }
</style>
</head>
<body>
  <section class="card card--front">
    <div class="texture" role="img" aria-label="Soft blue speckled texture"></div>
    <div class="brand">Marlow Hire</div>
  </section>

  <section class="card card--back">
    <div class="texture" role="img" aria-label="Faint blue speckled texture"></div>
    <div class="brand">Marlow Hire</div>
    <div class="person">
      <h1 class="person__name">Clara Whitfield</h1>
      <p class="person__role">Director | Senior Search Consultant</p>
    </div>
    <div class="divider"></div>
    <ul class="contacts">
      <li>
        <svg viewBox="0 0 16 16" aria-hidden="true"><path d="M1 3h14v10H1z M2 4.5v.6l6 4 6-4v-.6z" fill-rule="evenodd"/></svg>
        clara@marlowhire.nz
      </li>
      <li>
        <svg viewBox="0 0 16 16" aria-hidden="true"><path d="M3.6 1.2l2.3 2.6-1.3 1.8c.9 2 2.5 3.6 4.5 4.6l1.7-1.4 2.7 2.2-1.6 2.6C6.6 13.8 2.2 9.4 1.2 3.2z"/></svg>
        +64 27 480 2291
      </li>
    </ul>
    <div class="website">www.marlowhire.nz</div>
  </section>
</body>
</html>
```